Bramblecourt Homes Stationary
Fast Settlements
Professional
Dorian Pelletier
Managing Member
4817 Larkspur Ave Suite 210
Washington, DC
dgpelletier@bramblecourthomes.net
www.bramblecourthomes.net
Business License # 782645113058
Cash Buyer, Fast Closing.
Residential and Commercial
We are a Nation Wide Buyer.
will upload ai file shortly
vector logo file

```html
<!DOCTYPE html>
<html lang="en">
<head>
<meta charset="utf-8">
<title>Bramblecourt Homes Stationery</title>
<link href="https://fonts.googleapis.com/css2?family=Michroma&family=Open+Sans:wght@400;600&display=swap" rel="stylesheet">
<style>
:root{
  --green:#1a9a3a;
  --green-dark:#127a2c;
  --green-light:#2fb04d;
  --paper:#ffffff;
  --backdrop:#eceeed;
  --ink:#4a4a4a;
  --band:#eef0ef;
}
*{box-sizing:border-box;margin:0;padding:0}
html,body{width:1200px;height:936px;overflow:hidden}
body{background:var(--backdrop);position:relative;font-family:"Open Sans",sans-serif;color:var(--ink)}
.piece{position:absolute;background:var(--paper);box-shadow:0 2px 6px rgba(0,0,0,.15);overflow:hidden}

/* wordmark: stacked name with a plain square */
.brand{font-family:"Michroma",sans-serif;color:var(--green);font-weight:400;text-transform:uppercase;display:flex;align-items:center;white-space:nowrap}
.brand .mark{display:inline-block;background:var(--green);flex:none}
.brand .name{display:flex;flex-direction:column;align-items:center}
.brand .word{letter-spacing:.02em;line-height:1.1}
.brand .sub{font-size:.5em;letter-spacing:.35em;line-height:1;margin-top:.35em;padding-top:.3em;border-top:1px solid var(--green);align-self:stretch;text-align:center}

.tiny{font-size:6px;line-height:8px;color:var(--ink);white-space:nowrap}

/* letterhead */
.letterhead{left:145px;top:55px;width:502px;height:625px}
.letterhead .brand{position:absolute;left:40px;top:40px;font-size:12px;gap:7px}
.letterhead .brand .mark{width:12px;height:12px}
.letterhead .contact{position:absolute;right:40px;top:42px;display:flex;gap:16px}
.letterhead .rule{position:absolute;left:40px;right:40px;bottom:30px;height:1px;background:#e3e6e4}
.letterhead .footer{position:absolute;left:0;right:0;bottom:0;height:18px;background:var(--green);color:#fff;font-size:7px;letter-spacing:.2em;display:flex;align-items:center;justify-content:center}

/* folder */
.folder{left:672px;top:40px;width:470px;height:650px;background:linear-gradient(180deg,var(--green-light),var(--green) 45%,var(--green-dark))}
.folder .band{position:absolute;left:0;right:0;top:250px;height:120px;background:linear-gradient(180deg,#fafafa,var(--band));display:flex;align-items:center;justify-content:center}
.folder .band .brand{font-size:22px;gap:12px}
.folder .band .brand .mark{width:20px;height:20px}
.folder .web{position:absolute;left:0;right:0;bottom:60px;text-align:center;color:#fff;font-family:"Michroma",sans-serif;font-size:10px;letter-spacing:.28em}

/* business cards */
.card{left:85px;width:170px;height:95px}
.card-front{top:705px}
.card-front .brand{position:absolute;left:12px;top:12px;font-size:7px;gap:5px}
.card-front .brand .mark{width:7px;height:7px}
.card-front .details{position:absolute;left:12px;top:42px;font-size:5.5px;line-height:7px;white-space:nowrap}
.card-front .strip{position:absolute;left:0;right:0;bottom:0;height:7px;background:var(--green)}
.card-back{top:815px;background:var(--green);color:#fff}
.card-back .lines{position:absolute;left:0;right:0;top:28px;text-align:center;font-size:6px;line-height:9px}

/* envelopes */
.envelope{top:762px;height:143px}
.env-front{left:268px;width:372px}
.env-front .brand{position:absolute;left:22px;top:18px;font-size:9px;gap:6px}
.env-front .brand .mark{width:9px;height:9px}
.env-front .address{position:absolute;left:22px;top:46px;font-size:5.5px;line-height:7px}
.env-back{left:665px;width:477px}
.env-back svg{position:absolute;inset:0}
.env-back .web{position:absolute;left:0;right:0;top:14px;text-align:center;color:#fff;font-size:6px;letter-spacing:.2em}
</style>
</head>
<body>

<section class="piece letterhead">
  <div class="brand"><span class="mark"></span><span class="name"><span class="word">Bramblecourt</span><span class="sub">Homes</span></span></div>
  <div class="contact">
    <div class="tiny">P (202) 555-0147<br>F (202) 555-0148<br>dgpelletier@bramblecourthomes.net</div>
    <div class="tiny">4817 Larkspur Ave Suite 210<br>Washington, DC</div>
  </div>
  <div class="rule"></div>
  <div class="footer">www.bramblecourthomes.net</div>
</section>

<section class="piece folder">
  <div class="band"><div class="brand"><span class="mark"></span><span class="name"><span class="word">Bramblecourt</span><span class="sub">Homes</span></span></div></div>
  <div class="web">www.bramblecourthomes.net</div>
</section>

<section class="piece card card-front">
  <div class="brand"><span class="mark"></span><span class="name"><span class="word">Bramblecourt</span><span class="sub">Homes</span></span></div>
  <div class="details">Dorian Pelletier, Managing Member<br>P (202) 555-0147<br>dgpelletier@bramblecourthomes.net<br>www.bramblecourthomes.net</div>
  <div class="strip"></div>
</section>

<section class="piece card card-back">
  <div class="lines">Cash Buyer, Fast Closing.<br>Residential and Commercial<br>We are a Nation Wide Buyer.<br>Business License # 782645113058</div>
</section>

<section class="piece envelope env-front">
  <div class="brand"><span class="mark"></span><span class="name"><span class="word">Bramblecourt</span><span class="sub">Homes</span></span></div>
  <div class="address">4817 Larkspur Ave Suite 210<br>Washington, DC</div>
</section>

<section class="piece envelope env-back">
  <svg width="477" height="143" viewBox="0 0 477 143" aria-hidden="true">
    <path d="M0 0H477V40L238.5 78L0 40Z" fill="#1a9a3a"/>
  </svg>
  <div class="web">www.bramblecourthomes.net</div>
</section>

</body>
</html>
```